App Design - Job Lantern Quokka

We require an App Design for our new App called 'Lantern Quokka'. This app is essentially an assistant to help Users prepare for job interviews, to help them get hired. <br/><br/>Users who download the App can view common Questions and Answers, save their favourite responses and also view common Interview Tips. <br/><br/>The vision for our App is for Users who are preparing for an interview (1 week before, 1 day before, even 1 hour before), are able to download, view and educate themselves on common questions and responses, and then be confident to land the job. <br/><br/>Our team has developed wireframes to help highlight what each screen should do and include. Please see attached document, which also highlights key requirements for the experience. Feel free to add/remove/edit what you see on these wireframes. Our preference is that you use Adobe XD please.<br/><br/>In terms of design guidelines, we want the experience to be simple, intuitive and 'memorable' to help Users to remember the questions/responses when they are in the interview. <br/><br/>The final design should communicate 'neat and clean professionalism'; we like the design of: marlo vane com au<br/><br/>Thank you for reading! Good luck !

Target Market(s)

Professional job seekers

Font styles to use
Sans Serif

Colors

Designer to choose colors to be used in the design.

Requirements
Must have
• Please see my PlanHive_UX file that I have uploaded
Nice to have
• Could you also please include some ideas on how we can incorporate Advertising into the app screens

```html
<!DOCTYPE html>
<html lang="en">
<head>
<meta charset="utf-8">
<title>Lantern Quokka – App Screens</title>
<link rel="stylesheet" href="https://fonts.googleapis.com/css2?family=Exo+2:wght@700&family=Open+Sans:wght@400;600;700&display=swap">
<style>
  :root {
    --stage: #e6eaee;
    --screen: #e3e6e9;
    --brand-dark: #0b6db4;
    --brand-light: #4bbdec;
    --text-muted: #8a8f94;
    --text-dark: #2b2f33;
    --white: #ffffff;
    --photo-top: #c9b8a4;
    --photo-bottom: #3a4350;
  }
  * { box-sizing: border-box; margin: 0; padding: 0; }
  html, body { width: 1200px; height: 813px; overflow: hidden; }
  body {
    background: var(--stage);
    font-family: "Open Sans", sans-serif;
    position: relative;
  }
  .screen {
    position: absolute;
    width: 298px;
    height: 639px;
    background: var(--screen);
    border-radius: 34px;
    overflow: hidden;
    box-shadow: 0 10px 30px rgba(0,0,0,.18);
  }
  .screen--intro { left: 86px; top: 65px; }
  .screen--menu { left: 452px; top: 115px; }
  .screen--categories { left: 818px; top: 69px; }

  .brand-mark {
    position: absolute; left: 50%; top: 40px; transform: translateX(-50%);
    width: 62px; height: 62px; border-radius: 50%;
    background: var(--brand-dark);
  }
  .brand-name {
    position: absolute; left: 0; right: 0; top: 114px; text-align: center;
    font-family: "Exo 2", sans-serif; font-weight: 700;
    font-size: 29px; line-height: 36px; color: var(--brand-dark);
    white-space: nowrap;
  }
  .intro-copy {
    position: absolute; left: 16px; right: 16px; top: 180px;
    text-align: center; color: var(--text-muted);
    font-size: 14px; line-height: 25px;
  }
  .pill {
    position: absolute; left: 50%; transform: translateX(-50%);
    height: 46px; border-radius: 23px;
    display: flex; align-items: center; justify-content: center;
    color: var(--white); font-family: "Exo 2", sans-serif; font-weight: 700;
    font-size: 15.5px; letter-spacing: .2px; white-space: nowrap;
    box-shadow: 0 3px 6px rgba(0,0,0,.12);
  }
  .pill--dark { background: var(--brand-dark); }
  .pill--light { background: var(--brand-light); }
  .pill--wide { width: 279px; }
  .pill--read { width: 136px; top: 407px; }
  .pill--category { width: 216px; justify-content: flex-start; padding-left: 30px; gap: 14px; font-size: 15px; }
  .pill--category svg { width: 32px; height: 32px; flex: none; }

  .photo {
    position: absolute; left: 0; right: 0; bottom: 0;
    background: linear-gradient(180deg, var(--photo-top), var(--photo-bottom));
  }
  .screen--intro .photo { height: 142px; }
  .screen--menu .photo { height: 137px; }
  .screen--categories .photo { height: 121px; }

  .back-link {
    position: absolute; left: 14px; top: 38px;
    display: flex; align-items: center; gap: 10px;
    font-size: 14px; line-height: 20px; color: var(--text-dark);
  }
  .section-title {
    position: absolute; left: 0; right: 0; top: 176px; text-align: center;
    font-weight: 600; font-size: 21px; line-height: 28px; color: var(--text-dark);
    white-space: nowrap;
  }
  .section-sub {
    position: absolute; left: 0; right: 0; top: 216px; text-align: center;
    font-size: 13.5px; line-height: 20px; color: var(--text-dark);
  }
  .view-all {
    position: absolute; left: 0; right: 0; top: 494px; text-align: center;
    font-family: "Exo 2", sans-serif; font-weight: 700; font-size: 14px; line-height: 18px;
    color: var(--text-dark); text-decoration: underline;
  }
</style>
</head>
<body>

<section class="screen screen--intro">
  <div class="brand-mark"></div>
  <div class="brand-name">LANTERN QUOKKA</div>
  <p class="intro-copy">Lorem ipsum dolor sit amet, consectetur adipiscing elied do eiusmod tempor incididunabore et dolore magna aliquuis ipsum suspendisse ultrices gravidisus commodo vive labore et dolore magna aliquuis ipsum suspendisse ultrices gravidisus commodo viverrra maecenas accumsan lacus vel facilisis.</p>
  <div class="pill pill--dark pill--read">READ MORE</div>
  <div class="photo" role="img" aria-label="Photo of job candidates in business attire seated in a row waiting for interviews"></div>
</section>

<section class="screen screen--menu">
  <div class="brand-mark"></div>
  <div class="brand-name">LANTERN QUOKKA</div>
  <div class="pill pill--dark pill--wide" style="top:219px">VIEW QUESTIONS &amp; RESPONSES</div>
  <div class="pill pill--light pill--wide" style="top:297px">MY QUESTION PORTFOLIO</div>
  <div class="pill pill--light pill--wide" style="top:358px">INTERVIEW TIPS</div>
  <div class="photo" role="img" aria-label="Photo of job candidates in business attire seated in a row waiting for interviews"></div>
</section>

<section class="screen screen--categories">
  <div class="back-link">
    <svg width="10" height="16" viewBox="0 0 10 16"><path d="M8 2 2 8l6 6" fill="none" stroke="#2b2f33" stroke-width="2"/></svg>
    BACK
  </div>
  <div class="brand-mark"></div>
  <div class="brand-name">LANTERN QUOKKA</div>
  <h2 class="section-title">View Questions &amp; Responses</h2>
  <p class="section-sub">Select Your Question Category</p>

  <div class="pill pill--dark pill--category" style="top:256px">
    <svg viewBox="0 0 34 34" fill="none" stroke="#fff" stroke-width="1.6"><circle cx="17" cy="14" r="9"/><path d="M11 22v8M23 22v8"/></svg>
    BEHAVIORAL
  </div>
  <div class="pill pill--dark pill--category" style="top:314px">
    <svg viewBox="0 0 34 34" fill="none" stroke="#fff" stroke-width="1.6"><circle cx="20" cy="13" r="9"/><path d="M13 20 4 29"/><path d="M17.5 10.5a2.5 2.5 0 1 1 3 2.5v2"/><circle cx="20.5" cy="18" r=".6" fill="#fff"/></svg>
    SITUATIONAL
  </div>
  <div class="pill pill--dark pill--category" style="top:370px">
    <svg viewBox="0 0 34 34" fill="none" stroke="#fff" stroke-width="1.6"><path d="M4 26 14 16l6 6-10 10zM30 8 20 18l-6-6L24 2z"/></svg>
    MOTIVATIONAL
  </div>
  <div class="pill pill--dark pill--category" style="top:428px">
    <svg viewBox="0 0 34 34" fill="none" stroke="#fff" stroke-width="1.6"><circle cx="17" cy="10" r="6"/><rect x="6" y="19" width="22" height="12" rx="2"/><circle cx="17" cy="25" r="1.5"/></svg>
    TECHNICAL
  </div>
  <div class="view-all">VIEW ALL</div>
  <div class="photo" role="img" aria-label="Photo of job candidates in business attire seated in a row waiting for interviews"></div>
</section>

</body>
</html>
```